Harbourline Refrigeration business card design

We would like a new design for our business card as we have a new logo.
We need generic business card to give our customers with our office details - with the option of making it individualized for each manager

Target Market(s)

Companies and homeowners

Industry/Entity Type

Air Conditioning

Contact Information for Business Card

We are not sure if we want single or double sided it will depend on the design we choose

Colors
33a6d7
0255a3

Requirements
Must have
• Logo
• phone: (08) 8721 5940
• email: harbourserve@tealnet.example
• website: www.harbourlinerefrigeration.example
• AU61420
• BLD472913
Nice to have
• Address - Shed 5/284 Tallis Rd, Whyalla Norrie SA 5608

```html
<!DOCTYPE html>
<html lang="en">
<head>
<meta charset="utf-8">
<title>Harbourline Refrigeration – Business Card</title>
<link href="https://fonts.googleapis.com/css2?family=Archivo:wght@400;600;800&family=Arimo:wght@400;700&family=Oswald:wght@400&display=swap" rel="stylesheet">
<style>
  :root {
    --navy: #1d3f7e;
    --brand-blue: #0255a3;
    --sky: #33a6d7;
    --card-white: #fbfbfb;
    --backdrop: #1e1f22;
    --ink: #1d3f7e;
  }
  * { box-sizing: border-box; margin: 0; padding: 0; }
  html, body {
    width: 1200px; height: 1200px; overflow: hidden;
    background: var(--backdrop);
  }
  .stage { position: relative; width: 1200px; height: 1200px; }
  .card {
    position: absolute; left: 160px; width: 880px; height: 520px;
    border-radius: 28px; overflow: hidden;
  }
  /* Back side */
  .card--back {
    top: 50px;
    background: linear-gradient(135deg, #1c4a95 0%, var(--brand-blue) 55%, #1f5fb0 100%);
  }
  .card--back .brand {
    position: absolute; left: 0; right: 0; top: 185px; text-align: center;
    color: #fff;
  }
  .brand__name {
    font-family: "Archivo", sans-serif; font-weight: 800;
    font-size: 62px; letter-spacing: 0.5px; line-height: 1;
  }
  .brand__dot {
    display: inline-block; width: 18px; height: 18px; border-radius: 50%;
    margin-left: 10px; vertical-align: 6px;
  }
  .card--back .brand__dot { background: #fff; }
  .brand__tagline {
    font-family: "Oswald", sans-serif; font-weight: 400;
    font-size: 18px; letter-spacing: 2px; margin-top: 10px;
  }
  .card--back .brand__tagline { color: #d6e4f5; }
  .card--back .web-spaced {
    position: absolute; left: 0; right: 0; bottom: 55px; text-align: center;
    color: #fff; font-family: "Arimo", sans-serif; font-weight: 700;
    font-size: 17px; letter-spacing: 11px;
  }
  /* Front side */
  .card--front { top: 630px; background: var(--card-white); }
  .card--front .rules { position: absolute; inset: 0; }
  .person { position: absolute; left: 52px; top: 58px; }
  .person__name {
    font-family: "Archivo", sans-serif; font-weight: 800; color: var(--ink);
    font-size: 38px; line-height: 1;
  }
  .person__role {
    font-family: "Archivo", sans-serif; font-weight: 600; color: var(--sky);
    font-size: 22px; margin-top: 4px; letter-spacing: 0.5px;
  }
  .card--front .brand {
    position: absolute; right: 40px; top: 130px; text-align: right; color: var(--ink);
  }
  .card--front .brand__name { font-size: 44px; }
  .card--front .brand__dot { background: var(--sky); width: 14px; height: 14px; vertical-align: 4px; }
  .card--front .brand__tagline { color: var(--sky); font-size: 16px; margin-top: 6px; }
  .contacts {
    position: absolute; left: 52px; top: 312px; list-style: none;
    font-family: "Arimo", sans-serif; color: var(--ink); font-size: 23px;
  }
  .contacts li { display: flex; align-items: center; gap: 14px; height: 36px; }
  .contacts svg { width: 22px; height: 22px; flex: none; }
  .licences {
    position: absolute; right: 30px; top: 380px; text-align: right;
    font-family: "Arimo", sans-serif; color: var(--ink); font-size: 25px; line-height: 1.2;
  }
</style>
</head>
<body>
<main class="stage">

  <section class="card card--back" aria-label="Business card, back side">
    <div class="brand">
      <div class="brand__name">Harbourline<span class="brand__dot"></span></div>
      <div class="brand__tagline">REFRIGERATION &amp; AIR CONDITIONING</div>
    </div>
    <p class="web-spaced">WWW.HARBOURLINEREFRIGERATION.EXAMPLE</p>
  </section>

  <section class="card card--front" aria-label="Business card, front side">
    <svg class="rules" width="880" height="520" viewBox="0 0 880 520" aria-hidden="true">
      <polygon points="330,128 440,128 448,142 330,142" fill="var(--navy)"/>
      <polyline points="440,135 540,258 850,258" fill="none" stroke="var(--navy)" stroke-width="2"/>
      <line x1="52" y1="455" x2="740" y2="455" stroke="var(--navy)" stroke-width="2"/>
      <polygon points="740,452 850,452 850,472 724,472" fill="var(--navy)"/>
    </svg>

    <div class="person">
      <h1 class="person__name">DANIEL HARTLEY</h1>
      <p class="person__role">MANAGING DIRECTOR</p>
    </div>

    <div class="brand">
      <div class="brand__name">Harbourline<span class="brand__dot"></span></div>
      <div class="brand__tagline">REFRIGERATION &amp; AIR CONDITIONING</div>
    </div>

    <ul class="contacts">
      <li>
        <svg viewBox="0 0 24 24" aria-hidden="true"><path fill="var(--sky)" d="M6.6 10.8a15 15 0 0 0 6.6 6.6l2.2-2.2c.3-.3.7-.4 1-.2 1.1.4 2.3.6 3.6.6.6 0 1 .4 1 1V20c0 .6-.4 1-1 1A17 17 0 0 1 3 4c0-.6.4-1 1-1h3.5c.6 0 1 .4 1 1 0 1.3.2 2.5.6 3.6.1.3 0 .7-.2 1z"/></svg>
        <span>(08) 8721 5940</span>
      </li>
      <li>
        <svg viewBox="0 0 24 24" aria-hidden="true"><rect x="2" y="5" width="20" height="14" rx="1" fill="var(--sky)"/><path d="M2 6l10 7 10-7" fill="none" stroke="#fff" stroke-width="1.6"/></svg>
        <span>harbourserve@tealnet.example</span>
      </li>
      <li>
        <svg viewBox="0 0 24 24" aria-hidden="true"><g fill="none" stroke="var(--sky)" stroke-width="1.6"><circle cx="12" cy="12" r="9.5"/><ellipse cx="12" cy="12" rx="4" ry="9.5"/><line x1="2.5" y1="12" x2="21.5" y2="12"/><line x1="4" y1="7" x2="20" y2="7"/><line x1="4" y1="17" x2="20" y2="17"/></g></svg>
        <span>www.harbourlinerefrigeration.example</span>
      </li>
    </ul>

    <div class="licences">
      <p>AU61420</p>
      <p>BLD472913</p>
    </div>
  </section>

</main>
</body>
</html>
```